Flyer-Design für Handelsfirma für Afro Kosmetik
Zielgruppe
Wir sind eine Handelsfirma für Afro Kosmetik und für Frauen mit lockigen Haaren. Zur Eröffnung unseres Stores suchen wir einen Flyer, der die Zielgruppe informiert
Aufgabenstellung
Der Flyer soll unterschiedliche und austauschbare Bilder auf der ersten Seite haben. Dabei soll es sich immer um ein Hauptbild handeln, dass die entsprechende Zielgruppe anspricht. Bild 1 = Afrikaner; Bild 2 weiße mit lockigem Haar, Bild 3 = Südländer oder Latinos mit dunklem lockigem Haar.. Der Flyer soll 2 Seiten haben und in DIN LANG sein. Auf der Rückseite des Flyers soll unser Standort mit einer Karte und Wegbeschreibung sein.

```html
<!DOCTYPE html>
<html lang="de">
<head>
<meta charset="utf-8">
<title>Amara-Lokken – Flyer DIN lang</title>
<link rel="stylesheet" href="https://fonts.googleapis.com/css2?family=Montserrat:wght@300;400;500&display=swap">
<style>
  :root {
    --stage: #b9baba;
    --paper: #f4f3f3;
    --ink: #111111;
    --night: #050505;
    --hair: #16181c;
    --skin: #7a4427;
    --skin-light: #b06a3e;
    --white: #ffffff;
    --map-land: #e2e0dc;
    --map-road: #c4c1bb;
  }
  * { box-sizing: border-box; margin: 0; padding: 0; }
  html, body { width: 692px; height: 1200px; overflow: hidden; }
  body {
    background: var(--stage);
    font-family: "Montserrat", Arial, sans-serif;
    color: var(--ink);
    position: relative;
  }
  .panel {
    position: absolute;
    top: 260px;
    width: 293px;
    height: 679px;
    overflow: hidden;
  }
  .panel--front { left: 25px; background: var(--night); }
  .panel--back { left: 374px; background: var(--paper); }

  /* Front */
  .hero-photo {
    position: absolute; inset: 0;
    background:
      radial-gradient(ellipse 95% 40% at 65% 18%, var(--skin-light) 0%, var(--skin) 45%, transparent 75%),
      linear-gradient(180deg, #3a2013 0%, #1a0e08 35%, var(--night) 42%, var(--hair) 70%, var(--night) 100%);
  }
  .service-frame {
    position: absolute;
    left: 37px; top: 218px;
    width: 126px; height: 121px;
    left: 37px;
  }
  .service-frame {
    left: 37px; top: 218px; width: 126px; height: 121px;
  }
  .service-box {
    position: absolute;
    left: 37px; top: 218px;
    width: 126px; height: 121px;
    border: 1px solid rgba(255,255,255,0.55);
  }
  .service-list {
    position: absolute; left: 0; right: 0; top: 234px;
    list-style: none; text-align: center;
    color: var(--white);
    font-weight: 300; font-size: 9.5px; letter-spacing: 2.6px;
  }
  .service-list li { height: 24.5px; line-height: 16px; }
  .front-brand {
    position: absolute; left: 0; right: 0; top: 378px;
    text-align: center; color: #c9b36a;
    font-weight: 300; font-size: 21px; letter-spacing: 0.5px;
  }
  .front-url {
    position: absolute; left: 0; right: 0; top: 412px;
    text-align: center; color: var(--white);
    font-weight: 300; font-size: 7px; letter-spacing: 2px;
  }

  /* Back */
  .back-brand {
    position: absolute; left: 0; right: 0; top: 30px;
    text-align: center; font-weight: 300; font-size: 24px; letter-spacing: 0.5px;
  }
  .section-band {
    position: absolute; left: 0; right: 0; height: 24px;
    background: var(--night); color: var(--white);
    text-align: center; line-height: 24px;
    font-weight: 400; font-size: 9px; letter-spacing: 2.6px;
  }
  .section-band--services { top: 88px; }
  .section-band--membership { top: 262px; }
  .section-band--location { top: 424px; }
  .price-list { position: absolute; left: 32px; right: 31px; top: 128px; list-style: none; }
  .price-row {
    display: flex; align-items: baseline;
    height: 24.8px; font-size: 10.5px; letter-spacing: 0.4px;
  }
  .price-row__leader { flex: 1; border-bottom: 1px dotted #555; margin: 0 3px 3px 1px; min-width: 10px; }
  .price-row__from { font-size: 6.3px; letter-spacing: 0.2px; margin-right: 8px; }
  .price-row__price { width: 42px; text-align: right; }
  .tiers {
    position: absolute; left: 0; right: 0; top: 298px;
    list-style: none; display: flex; justify-content: space-around; padding: 0 20px;
    text-align: center;
  }
  .tier__name { font-size: 10px; letter-spacing: 0.5px; line-height: 16px; }
  .tier__price { font-size: 13px; letter-spacing: 0.5px; line-height: 20px; }
  .tiers-note {
    position: absolute; left: 0; right: 0; top: 350px;
    border-top: 1px solid #d6d4d2; margin: 0 32px;
  }
  .location {
    position: absolute; left: 20px; right: 20px; top: 462px;
    display: flex; gap: 12px;
  }
  .location__map {
    width: 120px; height: 92px; flex: none;
    border: 1px solid var(--ink);
  }
  .location__text { font-size: 8.5px; line-height: 13px; letter-spacing: 0.3px; }
  .location__address { font-weight: 500; margin-bottom: 5px; }
  .contact-rule { position: absolute; left: 0; right: 0; top: 572px; border-top: 1px solid var(--ink); }
  .contact { position: absolute; left: 0; right: 0; top: 589px; text-align: center; }
  .contact__label { font-size: 10.5px; letter-spacing: 0.5px; }
  .contact__phone { font-size: 18px; letter-spacing: 0.8px; margin-top: 6px; }
  .contact__hours { font-size: 10px; letter-spacing: 0.4px; margin-top: 4px; }
</style>
</head>
<body>
  <section class="panel panel--front">
    <div class="hero-photo" role="img" aria-label="Porträt einer Frau mit grün-silbernem Lidschatten über dunklen, lockigen Haaren"></div>
    <div class="service-box" style="left:77px;top:322px;width:186px;height:178px;left:54px;"></div>
    <ul class="service-list" style="top:344px;font-size:13.5px;letter-spacing:3.6px;">
      <li style="height:36.5px;line-height:26px;">HAARPFLEGE</li>
      <li style="height:36.5px;line-height:26px;">EXTENSIONS</li>
      <li style="height:36.5px;line-height:26px;">HAUTPFLEGE</li>
      <li style="height:36.5px;line-height:26px;">KOSMETIK</li>
    </ul>
    <div class="front-brand" style="top:566px;font-size:24px;">Amara-Lokken</div>
    <div class="front-url" style="top:622px;font-size:9.5px;letter-spacing:2.6px;">AMARA-LOKKEN.DE</div>
  </section>

  <section class="panel panel--back">
    <div class="back-brand">Amara-Lokken</div>

    <div class="section-band section-band--services">DIENSTLEISTUNGEN</div>
    <ul class="price-list">
      <li class="price-row"><span>HAARPFLEGE</span><span class="price-row__leader"></span><span class="price-row__from">BEGINNT VON</span><span class="price-row__price">1,65 €</span></li>
      <li class="price-row"><span>EXTENSIONS</span><span class="price-row__leader"></span><span class="price-row__from">BEGINNT VON</span><span class="price-row__price">25,50 €</span></li>
      <li class="price-row"><span>HAUTPFLEGE</span><span class="price-row__leader"></span><span class="price-row__from">BEGINNT VON</span><span class="price-row__price">7,50 €</span></li>
      <li class="price-row"><span>KOSMETIK</span><span class="price-row__leader"></span><span class="price-row__from">BEGINNT VON</span><span class="price-row__price">1,75 €</span></li>
      <li class="price-row"><span>ACCESSOIRES</span><span class="price-row__leader"></span><span class="price-row__from">BEGINNT VON</span><span class="price-row__price">0,50 €</span></li>
    </ul>

    <div class="section-band section-band--membership">MITGLIEDSCHAFT</div>
    <ul class="tiers">
      <li class="tier"><div class="tier__name">PLATINUM</div><div class="tier__price">200,00 €</div></li>
      <li class="tier"><div class="tier__name">GOLD</div><div class="tier__price">165,00 €</div></li>
      <li class="tier"><div class="tier__name">SILVER</div><div class="tier__price">95,00 €</div></li>
    </ul>

    <div class="section-band section-band--location">STANDORT</div>
    <div class="location">
      <svg class="location__map" viewBox="0 0 120 92" role="img" aria-label="Lageplan des Stores mit Straßen und Standortmarkierung">
        <rect width="120" height="92" fill="#e2e0dc"/>
        <path d="M0 34 H120 M0 70 H120 M38 0 V92 M86 0 V92" stroke="#c4c1bb" stroke-width="6"/>
        <path d="M0 88 L120 10" stroke="#c4c1bb" stroke-width="3"/>
        <path d="M62 22 c-6 0 -10 4.5 -10 10 c0 7 10 16 10 16 s10 -9 10 -16 c0 -5.5 -4 -10 -10 -10 z" fill="#111111"/>
        <circle cx="62" cy="32" r="3.5" fill="#f4f3f3"/>
      </svg>
      <div class="location__text">
        <p class="location__address">LINDENSTRASSE 14<br>24103 KIEL</p>
        <p>Ab Hauptbahnhof 5 Min. zu Fuß über die Holstenstraße, dann links.</p>
        <p>Bus 11 bis Haltestelle Lindenplatz.</p>
      </div>
    </div>

    <div class="contact-rule"></div>
    <div class="contact">
      <div class="contact__label">TELEPHONE SUPPORT AND ADVICE ON:</div>
      <div class="contact__phone">0431 - 582 904 16</div>
      <div class="contact__hours">MON-FRI, 12:30 PM - 6:30 PM</div>
    </div>
  </section>
</body>
</html>
```